Birthday Party Invitation

I need to create a "save the date" for my birthday party.
Text:

Save the Date
Saturday, 6 December 2014
9 pm
Club la Brisa, Lindenweg 42, 8005 Zürich
BLACK IT OUT
SAVE IT!
RESERVE THE TIME
WRITE IT DOWN
HOLD THE DATE to LET YOUR HAIR DOWN and Party with Me.

Target Market(s)

Friends

Industry/Entity Type

Club

Requirements
Must have
• I want the flyer to look classy and sexy at the same time.
Nice to have
• Picture on the left or right, then text white on black background. Maybe a simple frame. Not too playful, rather simple, elegant and no graphics. Just picture and text.

```html
<!DOCTYPE html>
<html lang="en">
<head>
<meta charset="utf-8">
<title>Save the Date – Birthday Party</title>
<link rel="stylesheet" href="https://fonts.googleapis.com/css2?family=Montserrat:wght@300;400;700&family=Raleway:wght@100;200&display=swap">
<style>
  :root {
    --page: #ffffff;
    --card: #000000;
    --ink: #ffffff;
    --ink-muted: #9a9a9a;
    --accent: #d0141c;
    --rule-light: #ffffff;
    --rule-dark: #555555;
    --photo-deep: #1a0a06;
  }
  * { margin: 0; padding: 0; box-sizing: border-box; }
  html, body {
    width: 1200px; height: 1000px; overflow: hidden;
    background: var(--page);
  }
  .invite {
    position: absolute; left: 50px; top: 280px;
    width: 1100px; height: 440px;
    background: var(--card);
    overflow: hidden;
    color: var(--ink);
  }
  .invite__photo {
    position: absolute; left: 0; top: 0;
    width: 415px; height: 100%;
    background:
      radial-gradient(ellipse 60% 65% at 45% 50%, rgba(160,50,35,0.85) 0%, rgba(90,30,18,0.7) 45%, rgba(0,0,0,0) 80%),
      radial-gradient(circle at 25% 30%, #4a2a1a 0%, var(--photo-deep) 60%, #000 100%);
  }
  .invite__rule {
    position: absolute; display: block; height: 4px;
  }
  .invite__rule--top { left: 415px; top: 18px; width: 655px; }
  .invite__rule--bottom { left: 415px; top: 222px; width: 655px; }

  .headline {
    position: absolute; left: 408px; top: 34px;
    width: 662px;
    font-family: "Raleway", sans-serif; font-weight: 100;
    font-size: 88px; letter-spacing: 0; line-height: 1;
    white-space: nowrap;
  }
  .details {
    position: absolute; left: 420px; top: 138px;
    font-family: "Montserrat", sans-serif; white-space: nowrap;
    line-height: 1;
  }
  .details__day { font-weight: 700; font-size: 30px; }
  .details__date { font-weight: 300; font-size: 30px; letter-spacing: 1px; }
  .details__time { font-weight: 700; font-size: 30px; }
  .details__sep {
    display: inline-block; width: 3px; height: 30px;
    background: var(--accent); margin: 0 18px; vertical-align: -4px;
  }
  .venue {
    position: absolute; left: 445px; top: 185px;
    font-family: "Montserrat", sans-serif; font-weight: 400;
    font-size: 17px; letter-spacing: 3.2px; white-space: nowrap;
    text-transform: uppercase;
  }
  .call {
    position: absolute; font-family: "Montserrat", sans-serif;
    white-space: nowrap; line-height: 1;
  }
  .call--black { left: 463px; top: 268px; font-weight: 700; font-size: 31px; }
  .call--reserve {
    left: 578px; top: 296px; font-family: "Raleway", sans-serif;
    font-weight: 200; font-size: 46px;
  }
  .call--write { left: 523px; top: 343px; }
  .call__thin {
    font-family: "Raleway", sans-serif; font-weight: 200;
    font-size: 29px; color: var(--ink-muted);
  }
  .call__bold { font-weight: 700; font-size: 21px; margin-left: 6px; }
  .call--party { left: 460px; top: 376px; font-weight: 700; font-size: 21px; }
</style>
</head>
<body>
  <section class="invite">
    <div class="invite__photo" role="img" aria-label="Photo of the host in a red and white festive costume"></div>

    <svg class="invite__rule invite__rule--top" viewBox="0 0 655 4" preserveAspectRatio="none" aria-hidden="true">
      <defs>
        <linearGradient id="ruleFade" x1="0" x2="1">
          <stop offset="0" stop-color="#555555"/>
          <stop offset="1" stop-color="#ffffff"/>
        </linearGradient>
      </defs>
      <rect width="655" height="3" fill="url(#ruleFade)"/>
    </svg>

    <h1 class="headline">SAVE THE DATE</h1>

    <p class="details">
      <span class="details__day">SATURDAY</span><span class="details__sep"></span><span class="details__date">6 DECEMBER 2014</span><span class="details__sep"></span><span class="details__time">9 PM</span>
    </p>
    <p class="venue">Club la Brisa, Lindenweg 42, 8005 Zürich</p>

    <svg class="invite__rule invite__rule--bottom" viewBox="0 0 655 4" preserveAspectRatio="none" aria-hidden="true">
      <rect width="655" height="3" fill="url(#ruleFade)"/>
    </svg>

    <p class="call call--black">BLACK IT OUT</p>
    <p class="call call--reserve">RESERVE THE TIME</p>
    <p class="call call--write"><span class="call__thin">WRITE IT DOWN</span><span class="call__bold">HOLD THE DATE</span></p>
    <p class="call call--party">to LET YOUR HAIR DOWN and Party with Me.</p>
  </section>
</body>
</html>
```